Personal Injury Lawyer Billboard

I would like a design created featuring the image of the lawyer centered in the middle of the design.
To the left of the lawyer's image it should read "INJURED?"
To the right of the lawyer's image, it should read "CALL BRUNO!"
Under Call Bruno, include the phone number 318-555-0187.
At the bottom of the design include the lawyers information "Bruno Pemberly Accident & Injury Lawyers"
PLEASE REMOVED THE BACKGROUND IMAGERY OF THE PHOTO SUBMITTED. Also, the colors for this design should match the colors shown in the logo (navy, white and relective soft gold). Please use those color combinations in ways that best stand out.

```html
<!DOCTYPE html>
<html lang="en">
<head>
<meta charset="utf-8">
<title>Injured? Call Bruno! – Billboard</title>
<link rel="stylesheet" href="https://fonts.googleapis.com/css2?family=Anton&family=Archivo+Black&family=Roboto+Condensed:wght@700&display=swap">
<style>
  :root {
    --navy: #002466;
    --white: #ffffff;
    --gold-light: #e8d671;
    --gold-dark: #b89a3e;
    --suit: #1e3470;
  }
  html, body {
    margin: 0;
    padding: 0;
    width: 1200px;
    height: 591px;
    overflow: hidden;
    background: var(--white);
  }
  .billboard {
    display: block;
    width: 1200px;
    height: 591px;
  }
  .headline-injured {
    font-family: "Anton", "Impact", sans-serif;
    fill: var(--navy);
  }
  .headline-call {
    font-family: "Archivo Black", "Arial Black", sans-serif;
    fill: var(--navy);
    stroke: var(--white);
    stroke-width: 18px;
    stroke-linejoin: round;
    paint-order: stroke fill;
  }
  .phone-number {
    font-family: "Roboto Condensed", "Arial Narrow", sans-serif;
    font-weight: 700;
    fill: var(--white);
    stroke: var(--navy);
    stroke-width: 5px;
    stroke-linejoin: round;
    paint-order: stroke fill;
  }
  .firm-name {
    font-family: "Roboto Condensed", "Arial Narrow", sans-serif;
    font-weight: 700;
    fill: var(--white);
  }
</style>
</head>
<body>
<svg class="billboard" viewBox="0 0 1200 591" xmlns="http://www.w3.org/2000/svg">
  <defs>
    <linearGradient id="goldSheen" x1="0" y1="0" x2="1" y2="0">
      <stop offset="0" stop-color="var(--gold-dark)"/>
      <stop offset="0.38" stop-color="var(--gold-light)"/>
      <stop offset="1" stop-color="var(--gold-dark)"/>
    </linearGradient>
    <linearGradient id="portraitTone" x1="0" y1="0" x2="0" y2="1">
      <stop offset="0" stop-color="#2f3550"/>
      <stop offset="0.45" stop-color="#3a4a80"/>
      <stop offset="1" stop-color="var(--suit)"/>
    </linearGradient>
  </defs>

  <rect class="band-gold" x="0" y="0" width="1200" height="386" fill="url(#goldSheen)"/>
  <polygon class="band-white" points="0,68 1200,179 1200,380 0,298" fill="var(--white)"/>
  <rect class="band-navy" x="0" y="386" width="1200" height="205" fill="var(--navy)"/>

  <rect class="lawyer-portrait" role="img" aria-label="Portrait of the attorney in a navy suit and green tie, smiling with a raised fist"
        x="520" y="47" width="270" height="544" fill="url(#portraitTone)"/>

  <text class="headline-injured" x="42" y="272" font-size="172" textLength="466" lengthAdjust="spacingAndGlyphs" transform="rotate(4 42 272)">INJURED?</text>

  <text class="headline-call" x="797" y="165" font-size="124" textLength="228" lengthAdjust="spacingAndGlyphs">CALL</text>
  <text class="headline-call" x="801" y="310" font-size="170" textLength="372" lengthAdjust="spacingAndGlyphs">BRUNO!</text>

  <text class="phone-number" x="592" y="522" font-size="112" textLength="545" lengthAdjust="spacingAndGlyphs">318-555-0187</text>

  <text class="firm-name" x="69" y="480" font-size="46" textLength="308" lengthAdjust="spacingAndGlyphs">BRUNO PEMBERLY</text>
  <text class="firm-name" x="69" y="520" font-size="26" textLength="307" lengthAdjust="spacingAndGlyphs">ACCIDENT &amp; INJURY LAWYERS</text>
</svg>
</body>
</html>
```